High end bathroom & wetroom supply and installation uk company require an A4 folded brochure

We have a website "larchandtide.com" this shows the market we are aiming at i.e. higher end

The brochure will be a fold out A4 ( three internal pages and front and rear cover) it will have lots of imagery ( we can supply photographs of our projects) and also incorporate a "design sketch" element on the "design" page - the internal pages of the brochure will be headed - page 1 - design, page 2 "supply" - page 3 ' install"
( see website - this will give a better idea)

The brochures purpose is to show potential clients ( private clients / architects / property developers) that we offer a comprehensive design service - a comprehensive supply service - and a professional installation service

We will provide wording - there will only be a few paragraphs - the images are the key to the impact of the brochure which will be printed on high quality gloss heavyweight paper/card
Updates

Apologies for confusion, my fault :-(

The brochure will be an A4 gatefold ( finished size A4) which would indeed be six sides ( inc front and rear covers) 

I'll upload photos etc tomorrow - I like the idea of the text ( which will be very similar to what is on the website) to be laid on top of the image rather than in a separate text box. 

I like the idea of the brochure looking like the website.

Hope that helps - 

this image shows the brochure type

www.printquiverworks.co.uk/assets/images/6PP_A4BrochurePlan.gif

Industry/Entity Type

It Company

Requirements
Must have
• when the a4 gate fold is open i.e. you are looking at three a4 pages they should be headed as;
page 1 - design
page 2 - supply
page 3 - install

A4 gate fold -A4 finished size

```html
<!DOCTYPE html>
<html lang="en">
<head>
<meta charset="utf-8">
<title>Larch &amp; Tide — A4 Gatefold Brochure</title>
<link rel="stylesheet" href="https://fonts.googleapis.com/css2?family=Josefin+Sans:wght@400;600&display=swap">
<style>
  :root {
    --stage: #262626;
    --paper: #f4f3f1;
    --ink-dark: #1f1f1f;
    --band: #2b2a28;
    --cover-wall: #4a4946;
    --cover-wall-deep: #34332f;
    --bath-white: #e9e8e4;
    --window-green: #6f8a5a;
    --stone-warm: #a8896a;
    --stone-deep: #6d5642;
    --text-light: #f2efe9;
    --text-muted: #cfc8bd;
  }
  * { box-sizing: border-box; margin: 0; padding: 0; }
  html, body { width: 1200px; height: 837px; overflow: hidden; }
  body {
    background: var(--stage);
    font-family: "Josefin Sans", "Gill Sans", sans-serif;
    position: relative;
  }
  .brochure {
    position: absolute;
    left: 24px; top: 227px;
    display: flex; gap: 24px;
  }
  .page {
    position: relative;
    width: 270px; height: 382px;
    background: var(--paper);
    overflow: hidden;
  }

  /* Front cover */
  .cover { background: var(--cover-wall); }
  .cover-photo {
    position: absolute; inset: 0;
    background: linear-gradient(180deg, var(--cover-wall) 0%, var(--cover-wall-deep) 38%, #3b3a37 60%, #d9d7d2 78%, #8d8b86 100%);
  }
  .cover-band {
    position: absolute; left: 0; right: 0; top: 150px; height: 70px;
    background: rgba(30, 30, 28, 0.75);
    display: flex; align-items: center; justify-content: center; gap: 10px;
  }
  .brand-name {
    color: var(--text-light);
    font-weight: 600; font-size: 22px; letter-spacing: 3px;
  }
  .brand-mark { width: 8px; height: 8px; background: var(--text-light); }
  .cover-footer {
    position: absolute; left: 0; right: 0; bottom: 0; height: 26px;
    background: var(--band);
    color: var(--text-muted); font-size: 8px; letter-spacing: 3px;
    display: flex; align-items: center; justify-content: center;
  }

  /* Inside pages */
  .inner { padding: 10px; }
  .page-head {
    position: absolute; top: 10px; left: 10px; right: 10px; height: 26px;
    display: flex; align-items: flex-end;
  }
  .page-title {
    background: var(--paper); color: var(--ink-dark);
    font-size: 11px; font-weight: 600; letter-spacing: 4px;
    padding: 6px 14px 5px 6px; text-transform: uppercase;
  }
  .page-photo { position: absolute; top: 36px; left: 10px; right: 10px; bottom: 10px; }
  .page-sub {
    position: absolute; top: 36px; left: 10px; right: 10px; height: 16px;
    background: rgba(244, 243, 241, 0.85);
    color: var(--ink-dark); font-size: 6.5px; letter-spacing: 2.5px;
    text-transform: uppercase; display: flex; align-items: center; padding-left: 8px;
  }
  .copy {
    position: absolute; left: 20px; right: 20px;
    color: var(--text-light); font-size: 8px; line-height: 1.55;
  }
  .copy p + p { margin-top: 6px; }
  .inset {
    position: absolute; border: 3px solid var(--paper);
  }

  .design .page-photo {
    background: linear-gradient(180deg, #d8dcd2 0%, var(--window-green) 30%, #4c5f3e 45%, #5d4c3c 55%, var(--stone-deep) 100%);
  }
  .design .copy { top: 200px; right: 120px; }
  .design .inset {
    right: 20px; top: 210px; width: 95px; height: 70px;
    background: linear-gradient(180deg, #c9cfc2, #8a9a7a 45%, #e4e1db 70%, #9c8468);
  }

  .supply .page-photo {
    background: linear-gradient(180deg, #55534f 0%, #3f3e3b 40%, #2f2e2c 55%, #d6d4cf 72%, #9f9d98 100%);
  }
  .supply .copy { top: 130px; left: 130px; right: 16px; }

  .install .page-photo {
    background: linear-gradient(160deg, var(--stone-warm) 0%, #bd9d7c 40%, #8b6f55 70%, var(--stone-deep) 100%);
  }
  .install .copy { top: 215px; right: 110px; }
  .install .inset {
    right: 20px; top: 225px; width: 85px; height: 95px;
    background: linear-gradient(180deg, #4a4a4a, #2d2d2d 50%, #e3e1dc 75%, #6e6a64);
  }
</style>
</head>
<body>
  <main class="brochure">
    <section class="page cover">
      <div class="cover-photo" role="img" aria-label="Photograph of a freestanding white bath before a dark grey wall with a candlelit shelf niche"></div>
      <div class="cover-band">
        <span class="brand-mark"></span>
        <span class="brand-name">LARCH &amp; TIDE</span>
      </div>
      <div class="cover-footer">WWW.LARCHANDTIDE.COM</div>
    </section>

    <section class="page inner design">
      <div class="page-photo" role="img" aria-label="Photograph of a bathroom beneath tall leaded windows overlooking green trees"></div>
      <div class="page-head"><span class="page-title">Design</span></div>
      <div class="page-sub">Bathroom &amp; Wetroom Design</div>
      <div class="copy">
        <p>Every project begins with a conversation about how you live, followed by measured plans and hand-drawn sketches of the space.</p>
        <p>We refine layouts, finishes and lighting until each detail feels right.</p>
      </div>
      <div class="inset" role="img" aria-label="Photograph of a freestanding bath under an arched window"></div>
    </section>

    <section class="page inner supply">
      <div class="page-photo" role="img" aria-label="Photograph of a white freestanding bath with a floor-mounted chrome filler and candlelit niche"></div>
      <div class="page-head"><span class="page-title">Supply</span></div>
      <div class="page-sub">Bathroom &amp; Wetroom Supply</div>
      <div class="copy">
        <p>We source sanitaryware, brassware, stone and tiles from trusted makers, delivered to site on your schedule.</p>
      </div>
    </section>

    <section class="page inner install">
      <div class="page-photo" role="img" aria-label="Photograph of a travertine-clad wetroom wall with chrome shower controls"></div>
      <div class="page-head"><span class="page-title">Install</span></div>
      <div class="page-sub">Bathroom &amp; Wetroom Installation</div>
      <div class="copy">
        <p>Our own fitters handle every stage, from first fix plumbing and tanking to the final polish of chrome.</p>
      </div>
      <div class="inset" role="img" aria-label="Photograph of a white basin on a dark vanity unit"></div>
    </section>
  </main>
</body>
</html>
```